Vantline Index Web Design

The vantlineindex-demo.net web site will be the source for unbiased economic performance expectations directly from the voice of business owners. Our Vantline Index survey effectively asks business owners "How's business?" The web site will present the resultant survey data, graphs, and reports to bankers and business owners. The overall goal is to help bankers better understand businesses of various sizes and industry types, as well as the direction in which our economy is heading by supplying them with the most current possible data.
Updates

Changes have been made to our list of requirements (and list of things the site should NOT include) so please review the briefing again. Thanks!

Reminder: the final deadline for this project isĀ Saturday, February 18, 2012 3:59 AM! Please get your submissions in by that time!

Target Market(s)

Bankers and Business Owners

Industry/Entity Type

Business

Requirements
Must have
• CSS stylesheet, incorporation an Vantline Index logo (could be based on the attached example, but rebranding is encouraged), intuitive navigation scheme based on the supplied flow chart, space to incorporate additional sponsor branding and/or advertising in the future
Nice to have
• Space to integrate Google Charts for the graphs representing research data
Should not have
• Incorporated elements from Quillby Analytics's main company website - the branding, look, feel, navigation and content of the Vantline Index Web site should be completely different and independent

```html
<!DOCTYPE html>
<html lang="en">
<head>
<meta charset="utf-8">
<title>Vantline Index</title>
<link href="https://fonts.googleapis.com/css2?family=Open+Sans:wght@400;600;700&family=Cormorant+Garamond:wght@400;500&display=swap" rel="stylesheet">
<style>
:root{
  --blue:#3f55d0;
  --blue-deep:#3a4fc9;
  --blue-light:#7f95ee;
  --ink:#111;
  --text:#222;
  --white:#fff;
  --rule:#cfcfcf;
  --grey:#9a9a9a;
  --bar:#5ab3c4;
}
*{margin:0;padding:0;box-sizing:border-box}
html,body{width:1200px;height:1143px;overflow:hidden}
body{position:relative;background:var(--white);font-family:"Open Sans",Arial,sans-serif;color:var(--text)}
.abs{position:absolute}

.site-header{position:absolute;left:0;top:0;width:1200px;height:119px;background:linear-gradient(#e6e6e6,#fafafa 60%,#fff)}
.brand{position:absolute;left:70px;top:28px;font-family:"Cormorant Garamond",Georgia,serif;font-size:30px;line-height:32px;color:var(--blue)}
.brand small{display:block;font-size:19px;color:var(--grey)}
.nav{position:absolute;left:408px;top:42px;height:77px;display:flex}
.nav a{display:flex;align-items:center;justify-content:center;height:77px;font-size:17px;color:var(--blue);text-decoration:none;border-right:1px solid var(--blue)}
.nav a.current{background:linear-gradient(#3d52cf,#6a80e8);color:var(--white);border-right:none}

.hero{position:absolute;left:0;top:119px;width:1200px;height:449px;background:linear-gradient(var(--blue-deep),var(--blue-light) 100%)}
.hero-copy{position:absolute;left:78px;top:36px;color:var(--white)}
.kicker{font-size:14.5px;line-height:20px}
.kicker span{color:var(--ink)}
.hero-title{margin-top:8px;font-size:32px;line-height:40px;font-weight:400;width:440px}
.hero-meta{position:absolute;left:85px;top:256px;color:var(--white);font-size:15.5px;line-height:24px}
.hero-meta strong{color:var(--ink);font-size:19px;display:block}
.btn{position:absolute;left:122px;top:340px;width:255px;height:41px;border-radius:10px;background:linear-gradient(#fff,#e4e4e4);color:var(--blue);font-size:17px;display:flex;align-items:center;justify-content:center;box-shadow:0 2px 4px rgba(0,0,0,.25)}
.feature-card{position:absolute;left:559px;top:36px;width:558px;height:349px;background:var(--white);box-shadow:0 1px 4px rgba(0,0,0,.3);font-family:"Cormorant Garamond",Georgia,serif;color:var(--blue)}
.feature-card .name{position:absolute;left:50px;top:96px;font-size:50px}
.feature-card .event{position:absolute;left:50px;top:175px;font-size:22px;line-height:24px}
.arrow{position:absolute;top:184px}

.tabs{position:absolute;left:42px;top:546px;width:1114px;height:104px;background:var(--white);box-shadow:0 1px 4px rgba(0,0,0,.25);display:flex}
.tabs .tab{position:relative;display:flex;align-items:center;justify-content:center;border-right:1px solid var(--rule)}
.tabs .tab:last-child{border-right:none}
.tab-pointer{position:absolute;left:155px;top:-12px;width:0;height:0;border-left:12px solid transparent;border-right:12px solid transparent;border-bottom:12px solid var(--white)}
.tab-label{font-family:"Cormorant Garamond",Georgia,serif;color:var(--blue);font-size:18px;line-height:18px}
.fast{font-family:"Open Sans",sans-serif;font-weight:700;font-size:18px;color:var(--blue)}

h2{font-weight:400;color:var(--blue);font-size:25px}
.welcome{position:absolute;left:40px;top:670px;width:690px}
.welcome p{margin-top:6px;font-size:15.8px;line-height:27.4px}
.sponsors{position:absolute;left:38px;top:855px;width:687px}
.sponsor-row{margin-top:8px;height:103px;border-top:1px solid var(--rule);border-bottom:1px solid var(--rule);display:flex;align-items:center;justify-content:space-between;padding:0 0 0 2px}
.sponsor{font-weight:700;font-size:17px;color:var(--blue)}

.graphs{position:absolute;left:773px;top:670px;width:385px}
.graphs p{margin-top:10px;font-size:14.8px;line-height:24px;color:var(--ink);padding-left:4px}

.site-footer{position:absolute;left:0;top:1026px;width:1200px;height:117px;background:linear-gradient(var(--blue-deep),var(--blue-light));color:var(--white)}
.address{position:absolute;left:41px;top:25px;font-size:12.5px;line-height:18.5px;font-style:normal}
.social{position:absolute;left:1032px;top:34px;display:flex;gap:10px}
.social span{width:22px;height:22px;border-radius:4px;background:var(--white);opacity:.9}
.copyright{position:absolute;right:48px;top:87px;font-size:12.5px}
</style>
</head>
<body>

<header class="site-header">
  <div class="brand">Vantline Index<small>Quillby Analytics</small></div>
  <nav class="nav">
    <a class="current" href="#" style="width:133px">Home</a>
    <a href="#" style="width:193px">Graphs &amp; Data</a>
    <a href="#" style="width:113px">Info</a>
    <a href="#" style="width:152px">Sponsors</a>
    <a href="#" style="width:159px">Get More</a>
  </nav>
</header>

<section class="hero">
  <div class="hero-copy">
    <p class="kicker">Register Today!<br><span>Quillby Analytics's February 2012 First Friday Web Conference</span></p>
    <h1 class="hero-title">"First Quarter 2012 Vantline Index Results: Temporary Exuberance"</h1>
  </div>
  <p class="hero-meta">Featuring Dana Whitcombe and Reid Quillby, Quillby Analytics<strong>Friday, February 3rd, 2012</strong>at Noon Eastern, 11 am Central, 9 am Pacific</p>
  <a class="btn">Details &amp; Registration</a>
  <div class="feature-card">
    <div class="name">Vantline Index</div>
    <div class="event">1st Friday<br>Web Conference</div>
  </div>
  <svg class="arrow" style="left:26px" width="40" height="40" viewBox="0 0 40 40"><circle cx="20" cy="20" r="19" fill="#fff"/><path d="M25 12 L14 20 L25 28" fill="none" stroke="#3f55d0" stroke-width="5"/></svg>
  <svg class="arrow" style="left:1138px" width="40" height="40" viewBox="0 0 40 40"><circle cx="20" cy="20" r="19" fill="#fff"/><path d="M15 12 L26 20 L15 28" fill="none" stroke="#3f55d0" stroke-width="5"/></svg>
</section>

<div class="tabs">
  <div class="tab-pointer"></div>
  <div class="tab" style="width:240px"><span class="tab-label">1st Friday<br>Web Conference</span></div>
  <div class="tab" style="width:192px"><div role="img" aria-label="Presentation board icon" style="width:44px;height:44px;background:linear-gradient(#e9ecf3,#b9c3d8);border-radius:3px"></div></div>
  <div class="tab" style="width:230px"><div role="img" aria-label="Analyst's journal illustration" style="width:60px;height:44px;background:#e6d9a6;border-radius:3px"></div></div>
  <div class="tab" style="width:232px"><div role="img" aria-label="Map of the United States by region" style="width:92px;height:56px;background:linear-gradient(90deg,#9a9a9a,#3f55d0 50%,#d9533b)"></div></div>
  <div class="tab" style="width:220px"><span class="fast">FAST FACTS</span></div>
</div>

<section class="welcome">
  <h2>Welcome</h2>
  <p>Quillby Analytics Associates, Inc. (QAAI) was founded in 1980 to provide research to the financial services industry. With a focus on business banking relationships, Quillby Analytics provides syndicated and custom solutions to the market research needs of the largest banks in the United States. If you have any questions about QAAI, its services, or market research related to business banking relationships, please contact us.</p>
</section>

<section class="sponsors">
  <h2>Sponsors</h2>
  <div class="sponsor-row">
    <span class="sponsor">Hartwell Media</span>
    <span class="sponsor">Orchard Floor Care</span>
    <span class="sponsor">Greenloop</span>
    <span class="sponsor">Netforge</span>
  </div>
</section>

<section class="graphs">
  <h2>Graphs &amp; Data</h2>
  <svg width="372" height="185" viewBox="0 0 372 185" style="margin-top:8px" font-family="Open Sans, sans-serif" font-size="7" fill="#333">
    <g stroke="#bbb" stroke-width="1">
      <line x1="30" y1="15" x2="365" y2="15"/><line x1="30" y1="44" x2="365" y2="44"/><line x1="30" y1="73" x2="365" y2="73"/><line x1="30" y1="102" x2="365" y2="102"/><line x1="30" y1="131" x2="365" y2="131"/>
    </g>
    <line x1="30" y1="160" x2="365" y2="160" stroke="#333"/>
    <g text-anchor="end"><text x="22" y="17">25</text><text x="22" y="46">20</text><text x="22" y="75">15</text><text x="22" y="104">10</text><text x="22" y="133">5</text><text x="22" y="162">0</text></g>
    <g fill="#5ab3c4">
      <rect x="42" y="121.1" width="18" height="38.9"/><rect x="84" y="110.1" width="18" height="49.9"/><rect x="126" y="122.9" width="18" height="37.1"/><rect x="168" y="28.9" width="18" height="131.1"/><rect x="210" y="23.7" width="18" height="136.3"/><rect x="252" y="102.6" width="18" height="57.4"/><rect x="294" y="93.3" width="18" height="66.7"/><rect x="336" y="68.4" width="18" height="91.6"/>
    </g>
    <g text-anchor="middle">
      <text x="51" y="117">6.7</text><text x="93" y="106">8.6</text><text x="135" y="119">6.4</text><text x="177" y="25">22.6</text><text x="219" y="20">23.5</text><text x="261" y="99">9.9</text><text x="303" y="90">11.5</text><text x="345" y="65">15.8</text>
      <text x="51" y="174">BC</text><text x="93" y="174">AB</text><text x="135" y="174">SK</text><text x="177" y="174">ON</text><text x="219" y="174">QC</text><text x="261" y="174">NB</text><text x="303" y="174">NL</text><text x="345" y="174">Canada</text>
    </g>
  </svg>
  <p>Lorem Ipsum is simply dummy text of the printing and typesetting industry. Lorem Ipsum has been the industry's standard dummy</p>
</section>

<footer class="site-footer">
  <address class="address">Quillby Analytics Associates, Inc.<br>482 Alder Court South<br>Brookfield, MN 55900<br>Tel: 555-014-2200 Fax: 555-014-2279</address>
  <div class="social" aria-label="Social links"><span></span><span></span><span></span><span></span></div>
  <p class="copyright">© Copyright 2012 All Rights Reserved</p>
</footer>

</body>
</html>
```